Business Card Design Project - bel soravin group

dear Sirs

we need business card design for our group ( BEL Soravin Group ) , i have got the Logo design of our group from pixel harbor in previous , so all need details relating to our group i think available with you, as well as the the chosen logo design

we hope to provide us with business card logo that to be appropaite and satisfactory to us .

thanks

note : logo design of our group is attached .
Updates

Reason: please extend the deadline of my project for additional 15 days because i didn't received appropriate design for our gruop yet . kindly beaware that i have received 77 design till now , supossed to send me 200-250 design at least . thanks

Target Market(s)

contents
-

name : Korvan EL Mistrani

position : Operation Manager

Industry/Entity Type

Business

Requirements
Must have

• person name

group logo
Nice to have
• logo color matching with back background

```html
<!DOCTYPE html>
<html lang="en">
<head>
<meta charset="utf-8">
<title>BEL Soravin Group – Business Card</title>
<link rel="stylesheet" href="https://fonts.googleapis.com/css2?family=Arimo:wght@400;700&family=Open+Sans:wght@800&family=Poppins:wght@500&display=swap">
<style>
  :root {
    --royal-blue: #0035c9;
    --card-edge: #2b3fe0;
    --paper: #ffffff;
    --sand-light: #f2e68d;
    --gold-deep: #bd8c00;
    --label-yellow: #f3e98c;
    --glow-center: #ffffff;
    --glow-edge: #0f3ad0;
  }
  * { margin: 0; padding: 0; box-sizing: border-box; }
  html, body { width: 875px; height: 1200px; overflow: hidden; background: var(--paper); }
  .sheet { position: relative; width: 875px; height: 1200px; }

  .card { position: absolute; left: 0; width: 875px; border-radius: 42px; overflow: hidden; }
  .card--front {
    top: 0; height: 567px; border: 2px solid var(--card-edge);
    background: linear-gradient(90deg, var(--paper) 0 260px, transparent 260px 505px, var(--royal-blue) 505px);
  }
  .card--back {
    top: 633px; height: 566px; border: 2px solid #6f7fe8;
    background: radial-gradient(ellipse 62% 70% at 48% 40%, var(--glow-center) 0%, #9fb0ee 45%, var(--glow-edge) 100%);
  }

  .card__accent {
    position: absolute; top: 0; bottom: 0; left: 260px; width: 245px;
    background: linear-gradient(90deg, var(--sand-light) 0%, #e0cf5e 50%, var(--gold-deep) 100%);
  }

  .brand {
    position: absolute; display: flex; align-items: center; gap: 12px;
    font-family: "Poppins", sans-serif; font-weight: 500; color: var(--royal-blue);
    white-space: nowrap; letter-spacing: 0.5px;
  }
  .brand__mark { background: var(--royal-blue); flex: none; }
  .brand--small { left: 48px; top: 80px; font-size: 26px; }
  .brand--small .brand__mark { width: 20px; height: 20px; }
  .brand--large { left: 50%; top: 250px; transform: translateX(-50%); font-size: 62px; gap: 20px; }
  .brand--large .brand__mark { width: 44px; height: 44px; }

  .holder {
    position: absolute; left: 693px; top: 176px; transform: translateX(-50%);
    text-align: center; white-space: nowrap; font-family: "Arimo", sans-serif; color: var(--paper);
  }
  .holder__name { font-size: 34px; font-weight: 700; line-height: 1.1; }
  .holder__role { font-size: 22px; font-weight: 400; margin-top: 2px; }

  .contact { position: absolute; list-style: none; font-family: "Open Sans", sans-serif; font-weight: 800; font-size: 22px; line-height: 28px; }
  .contact--phones { left: 45px; top: 434px; color: var(--royal-blue); }
  .contact--online { left: 546px; top: 434px; color: var(--label-yellow); }
</style>
</head>
<body>
<main class="sheet">
  <section class="card card--front" aria-label="Card front">
    <div class="card__accent" role="img" aria-label="Decorative gold sail-shaped swoosh accent"></div>

    <div class="brand brand--small">
      <span class="brand__mark"></span>
      <span class="brand__name">BEL SORAVIN GROUP</span>
    </div>

    <div class="holder">
      <h1 class="holder__name">Korvan EL Mistrani</h1>
      <p class="holder__role">Operation Manager</p>
    </div>

    <ul class="contact contact--phones">
      <li>tel :</li>
      <li>fax :</li>
      <li>mobile :</li>
    </ul>
    <ul class="contact contact--online">
      <li>email address :</li>
      <li>web site :</li>
      <li>PO . Box:</li>
    </ul>
  </section>

  <section class="card card--back" aria-label="Card back">
    <div class="brand brand--large">
      <span class="brand__mark"></span>
      <span class="brand__name">BEL SORAVIN</span>
    </div>
  </section>
</main>
</body>
</html>
```